JT & WE Shearing Pty Ltd

We already have an existing logo created by Lumen Quarry however we have restructured to a company. We would like someone to add Pty Ltd to our business name please.

Colors

Designer to choose only greyscale colors for use in the design.

```html
<!DOCTYPE html>
<html lang="en">
<head>
<meta charset="utf-8">
<title>JT &amp; WE Shearing Pty Ltd — Business Card</title>
<link rel="stylesheet" href="https://fonts.googleapis.com/css2?family=Playfair+Display:wght@700&family=Raleway:wght@400&display=swap">
<style>
  :root {
    --backdrop: #e6e4e1;
    --card: #f7f7f6;
    --card-edge: #dcdcdb;
    --ink-dark: #2f2f2f;
    --ink-mid: #555555;
    --rule: #8a8a8a;
    --icon-bg: #3a3a3a;
    --icon-fg: #ffffff;
  }
  * { margin: 0; padding: 0; box-sizing: border-box; }
  html, body {
    width: 1200px;
    height: 1022px;
    overflow: hidden;
    background: var(--backdrop);
  }
  .canvas {
    position: relative;
    width: 1200px;
    height: 1022px;
    display: flex;
    align-items: center;
    justify-content: center;
  }
  .business-card {
    width: 900px;
    height: 514px;
    background: var(--card);
    border: 1px solid var(--card-edge);
    border-radius: 22px;
    box-shadow: 0 18px 40px rgba(0,0,0,0.12);
    display: flex;
    align-items: center;
    padding: 0 70px 0 80px;
  }
  .brand {
    flex: 0 0 360px;
    font-family: "Playfair Display", serif;
    font-weight: 700;
    color: var(--ink-dark);
    text-transform: uppercase;
    line-height: 0.95;
  }
  .brand-initials { display: block; font-size: 92px; letter-spacing: -2px; }
  .brand-trade { display: block; font-size: 44px; letter-spacing: 1px; margin-top: 8px; }
  .brand-entity { display: block; font-size: 44px; letter-spacing: 3px; margin-top: 4px; }
  .divider {
    width: 1px;
    height: 150px;
    background: var(--rule);
    margin: 0 34px 0 30px;
  }
  .contact { flex: 1; }
  .contact-name {
    font-family: "Playfair Display", serif;
    font-weight: 700;
    font-size: 30px;
    letter-spacing: 3px;
    text-transform: uppercase;
    color: var(--ink-dark);
    margin-bottom: 16px;
  }
  .contact-list { list-style: none; }
  .contact-item {
    display: flex;
    align-items: center;
    gap: 12px;
    font-family: "Raleway", sans-serif;
    font-size: 20px;
    color: var(--ink-mid);
    line-height: 1.75;
  }
  .contact-icon { width: 18px; height: 18px; flex: 0 0 18px; }
</style>
</head>
<body>
<main class="canvas">
  <section class="business-card" aria-label="Business card, front">
    <div class="brand" aria-label="JT &amp; WE Shearing Pty Ltd">
      <span class="brand-initials">JT &amp; WE</span>
      <span class="brand-trade">Shearing</span>
      <span class="brand-entity">Pty Ltd</span>
    </div>
    <div class="divider"></div>
    <div class="contact">
      <h1 class="contact-name">Ned Harlowe</h1>
      <ul class="contact-list">
        <li class="contact-item">
          <svg class="contact-icon" viewBox="0 0 18 18" aria-hidden="true">
            <circle cx="9" cy="9" r="9" fill="var(--icon-bg)"/>
            <path d="M4.5 9 L9 5 L13.5 9 H12 V13 H6 V9 Z" fill="var(--icon-fg)"/>
          </svg>
          PO Box 418 KELLERBY WA 6512
        </li>
        <li class="contact-item">
          <svg class="contact-icon" viewBox="0 0 18 18" aria-hidden="true">
            <circle cx="9" cy="9" r="9" fill="var(--icon-bg)"/>
            <path d="M6 4.5 L7.8 4.5 L8.4 7 L7.3 7.9 Q8.3 10 10.1 10.7 L11 9.6 L13.5 10.2 L13.5 12 Q13 13.5 11.3 13.3 Q5.5 12 4.7 6.3 Q4.6 4.8 6 4.5 Z" fill="var(--icon-fg)"/>
          </svg>
          0491 572 204
        </li>
        <li class="contact-item">
          <svg class="contact-icon" viewBox="0 0 18 18" aria-hidden="true">
            <circle cx="9" cy="9" r="9" fill="var(--icon-bg)"/>
            <rect x="4.5" y="5.8" width="9" height="6.4" fill="none" stroke="var(--icon-fg)" stroke-width="1.2"/>
            <path d="M4.5 5.8 L9 9.4 L13.5 5.8" fill="none" stroke="var(--icon-fg)" stroke-width="1.2"/>
          </svg>
          jtweshearing@mailbay.com
        </li>
      </ul>
    </div>
  </section>
</main>
</body>
</html>
```